Letterhead for 3 attorney Workers' Comp law firm

We are a 3 attorney law office. We specialize in Workers' Compensation. Our office represents workers who are injured on the job, and the estates of workers who are killed one the job.
When we started our office, we created our own letterhead & have been using it for years. We've just recently hired the 3rd attorney, and were going to just add his name to the letterhead, but have decided we wanted to get a professionally designed letterhead and business cards at this point.
We want something that looks clean and professional. It must look good in black and white because we often make multiple copies of our documents. We're hoping for a design that resonates confidence, reliability and experience.
The design must include the firm name: Dorrance & Pike, PLLC. We would like the PLLC to be small compared to the Dorrance & Pike graphic. We also want to incorporate the attorney names: Ulric Dorrance, Janet Pike, and Lyle Hagberg. Our current letterhead has our contact info in the footer at the bottom of the page. We like that design, but are open to the idea of having it at the top. We'll leave that at the discretion of the designer. Our contact info is as follows: 472 S. Larchmont Avenue, Suite 315 Bellingham, WA 98117 Phone: 360-514-2967, Fax: 360-521-6079, and our website: www.dorrancepike-law.example
Target Market(s)
Clients, courts, other legal offices, doctors offices. These are the people who see our letterhead most frequently. It's not so much for marketing purposes, mainly so that we have a professional image when sending out documents.
Industry/Entity Type
Law Firm
Contact Information for Business Card
On the back of the business card: it can be designed, or be a template for filling in appointment reminder information (i.e. date, time, etc)
Colors
Designer to choose colors to be used in the design.
Requirements
Must have
- Must have our firm name at the top.
- Must include the attorney names.
- Must have all of our contact information (can be at top or bottom - whatever looks best with the design)
Nice to have
- A strong, confident design
Should not have
- We don't want the design to be playful, cartoony or busy.

```html
<!DOCTYPE html>
<html lang="en">
<head>
<meta charset="utf-8">
<title>Dorrance &amp; Pike, PLLC — Stationery</title>
<link rel="stylesheet" href="https://fonts.googleapis.com/css2?family=Arimo:wght@400;700&family=Tinos:ital@0;1&display=swap">
<style>
  :root {
    --navy: #26225f;
    --ink: #555558;
    --ink-dark: #333336;
    --paper: #ffffff;
    --backdrop: #dedede;
    --rule-grey: #9a9aa6;
  }
  html, body {
    margin: 0;
    padding: 0;
    width: 1200px;
    height: 840px;
    overflow: hidden;
    background: var(--backdrop);
  }
  .canvas {
    position: relative;
    width: 1200px;
    height: 840px;
    background: var(--backdrop);
    font-family: "Arimo", Arial, sans-serif;
    color: var(--ink);
  }

  /* Business card — front */
  .card {
    position: absolute;
    width: 300px;
    height: 172px;
    background: var(--paper);
    box-shadow: 0 2px 6px rgba(0,0,0,0.12);
    overflow: hidden;
  }
  .card--front { left: 110px; top: 120px; }
  .card--back  { left: 110px; top: 322px; }

  .card__panel {
    position: absolute;
    left: 0; top: 0;
    width: 116px; height: 100%;
    background: var(--navy);
  }
  .card__name {
    position: absolute;
    left: 14px; top: 94px;
    color: var(--paper);
    font-size: 13px;
    line-height: 1.15;
  }
  .card__name-last {
    display: block;
    font-weight: 700;
    letter-spacing: 0.5px;
  }
  .card__contact {
    position: absolute;
    right: 14px; top: 16px;
    width: 160px;
    font-family: "Tinos", "Times New Roman", serif;
    font-size: 8.5px;
    line-height: 1.45;
    color: var(--ink-dark);
    text-align: right;
  }
  .card__web {
    position: absolute;
    right: 14px; bottom: 12px;
    font-family: "Tinos", "Times New Roman", serif;
    font-size: 8.5px;
    color: var(--ink-dark);
  }

  /* Business card — back */
  .card__wordmark {
    position: absolute;
    left: 0; right: 0; top: 62px;
    text-align: center;
    font-size: 26px;
    color: var(--navy);
    letter-spacing: 0.5px;
  }
  .card__pllc {
    position: absolute;
    right: 34px; top: 96px;
    font-family: "Tinos", "Times New Roman", serif;
    font-size: 8px;
    color: var(--ink-dark);
  }

  /* Letterhead */
  .letterhead {
    position: absolute;
    left: 690px; top: 110px;
    width: 456px; height: 590px;
    background: var(--paper);
    box-shadow: 0 2px 8px rgba(0,0,0,0.12);
  }
  .letterhead__masthead {
    position: absolute;
    left: 0; right: 0; top: 40px;
    text-align: center;
  }
  .letterhead__wordmark {
    font-size: 22px;
    color: var(--navy);
    letter-spacing: 0.5px;
  }
  .letterhead__pllc {
    font-family: "Tinos", "Times New Roman", serif;
    font-size: 7px;
    color: var(--ink-dark);
    margin-left: 4px;
  }
  .letterhead__attorneys {
    margin-top: 6px;
    font-family: "Tinos", "Times New Roman", serif;
    font-size: 7px;
    color: var(--ink-dark);
  }
  .letterhead__rule {
    position: absolute;
    left: 28px; right: 28px; top: 510px;
    height: 3px;
    background: var(--navy);
    border-bottom: 1px solid var(--rule-grey);
  }
  .letterhead__address {
    position: absolute;
    left: 28px; top: 522px;
    font-family: "Tinos", "Times New Roman", serif;
    font-size: 7.5px;
    line-height: 1.5;
    color: var(--ink-dark);
  }
  .letterhead__address-label { font-style: italic; }
  .letterhead__reach {
    position: absolute;
    right: 28px; top: 522px;
    font-family: "Tinos", "Times New Roman", serif;
    font-size: 7.5px;
    line-height: 1.5;
    color: var(--ink-dark);
    text-align: right;
  }

  /* Primary lockup */
  .lockup {
    position: absolute;
    left: 56px; top: 610px;
    width: 560px;
  }
  .lockup__wordmark {
    font-size: 64px;
    line-height: 1;
    color: var(--navy);
    letter-spacing: 1px;
  }
  .lockup__pllc {
    position: absolute;
    left: 480px; top: 148px;
    font-family: "Tinos", "Times New Roman", serif;
    font-size: 13px;
    color: var(--ink-dark);
  }
  .lockup__attorneys {
    position: absolute;
    left: 0; top: 170px;
    font-family: "Tinos", "Times New Roman", serif;
    font-size: 17px;
    color: var(--ink-dark);
    white-space: nowrap;
  }
  .lockup__attorneys em { font-style: italic; }
</style>
</head>
<body>
<main class="canvas">

  <section class="card card--front" aria-label="Business card, front">
    <div class="card__panel">
      <p class="card__name">Ulric <span class="card__name-last">DORRANCE</span></p>
    </div>
    <address class="card__contact" style="font-style:normal">
      Phone: 360-514-2967<br>
      Fax: 360-521-6079<br>
      472 S. Larchmont Avenue, Suite 315<br>
      Bellingham, WA 98117
    </address>
    <p class="card__web" style="margin:0">www.dorrancepike-law.example</p>
  </section>

  <section class="card card--back" aria-label="Business card, back">
    <p class="card__wordmark" style="margin:0">Dorrance &amp; Pike</p>
    <span class="card__pllc">PLLC.</span>
  </section>

  <section class="letterhead" aria-label="Letterhead">
    <header class="letterhead__masthead">
      <span class="letterhead__wordmark">Dorrance &amp; Pike</span><span class="letterhead__pllc">PLLC.</span>
      <div class="letterhead__attorneys"><em>Attorneys</em> | Ulric DORRANCE, Janet PIKE, and Lyle HAGBERG</div>
    </header>
    <div class="letterhead__rule"></div>
    <footer>
      <p class="letterhead__address" style="margin:0">
        <span class="letterhead__address-label">Mailing Address</span><br>
        472 S. Larchmont Avenue, Suite 315<br>
        Bellingham, WA 98117
      </p>
      <p class="letterhead__reach" style="margin:0">
        Phone: 360-514-2967<br>
        Fax: 360-521-6079<br>
        www.dorrancepike-law.example
      </p>
    </footer>
  </section>

  <section class="lockup" aria-label="Firm name lockup">
    <div class="lockup__wordmark">Dorrance &amp; Pike</div>
    <span class="lockup__pllc">P.L.L.C.</span>
    <p class="lockup__attorneys" style="margin:0"><em>Attorneys</em> | Ulric DORRANCE, Janet PIKE, and Lyle HAGBERG</p>
  </section>

</main>
</body>
</html>
```